5th Battalion 42nd Cavalry Regiment " Grey Falcons"

Hello,
I am a lieutenant in the Northmark Defense Corps and my boss lieutenant colonel (commander) has asked me to come up with a business card for him. I threw a few designs toward him and he declined all of them. He really like the Knight business card background that is attached below(, but would like another Knight to replace it). We are 5th Battalion 42nd Cavalry Regiment (Grey Falcons is are Battalion Symbol) and are a Heavy Armored Combat team( Tanks and Carver's). He is an Infantry LTC would love a Bold but simple Grey Falcon riding on a horse. It doesn’t have to have the same back ground as the attached file named Finished Card, but will need all the information that is on both sides of the card. Thank you very much for your help and I look forward to seeing the designs.
V/R
Dale Whitcombe

Reason: My boss would like to see a few more designs.

```html
<!DOCTYPE html>
<html lang="en">
<head>
<meta charset="utf-8">
<title>Grey Falcon Unit Vision Card</title>
<link rel="stylesheet" href="https://fonts.googleapis.com/css2?family=Cinzel:wght@400;500&family=Cabin:wght@500&display=swap">
<style>
  :root {
    --paper: #ffffff;
    --camo-deep: #14240c;
    --camo-mid: #2f4a1a;
    --camo-light: #4f6e2a;
    --panel: rgba(14, 22, 10, 0.82);
    --title-bg: #1c2a12;
    --band: #1a2b10;
    --rule: #4d6a34;
    --glow: #b9e07a;
    --ink: #f4f4ee;
  }
  * { margin: 0; padding: 0; box-sizing: border-box; }
  html, body { width: 1200px; height: 702px; overflow: hidden; background: var(--paper); }
  .card {
    position: relative;
    width: 1200px;
    height: 702px;
    background: var(--paper);
  }
  .camo-field {
    position: absolute;
    left: 20px; top: 20px;
    width: 1160px; height: 663px;
    background:
      radial-gradient(ellipse at 20% 30%, var(--camo-light) 0%, transparent 45%),
      radial-gradient(ellipse at 75% 15%, var(--camo-mid) 0%, transparent 50%),
      radial-gradient(ellipse at 60% 80%, var(--camo-light) 0%, transparent 40%),
      linear-gradient(180deg, var(--camo-mid) 0%, var(--camo-deep) 100%);
  }
  .rider-photo {
    position: absolute;
    left: 44px; top: 62px;
    width: 300px; height: 520px;
    border-radius: 45% 45% 20% 20%;
    background: radial-gradient(ellipse at 50% 55%, #6f7b5a 0%, #2a3320 55%, rgba(185, 224, 122, 0.35) 75%, transparent 90%);
  }
  .vision-panel {
    position: absolute;
    left: 409px; top: 239px;
    width: 738px; height: 325px;
    background: var(--panel);
    border: 1px solid rgba(77, 106, 52, 0.5);
  }
  .vision-title {
    position: absolute;
    left: 543px; top: 200px;
    width: 508px; height: 77px;
    background: var(--title-bg);
    border: 1px solid var(--rule);
    display: flex; align-items: center; justify-content: center;
    font-family: "Cinzel", serif;
    font-weight: 400;
    font-size: 27px;
    letter-spacing: 0.5px;
    color: var(--ink);
  }
  .vision-text {
    position: absolute;
    left: 409px; top: 326px;
    width: 738px;
    text-align: center;
    font-family: "Cinzel", serif;
    font-weight: 500;
    font-size: 26px;
    line-height: 33px;
    letter-spacing: 1px;
    color: var(--ink);
    text-transform: lowercase;
  }
  .vision-text::first-letter { text-transform: uppercase; }
  .motto-band {
    position: absolute;
    left: 20px; top: 583px;
    width: 1160px; height: 65px;
    background: var(--band);
    border-top: 1px solid var(--rule);
    border-bottom: 1px solid var(--rule);
    display: flex; align-items: center; justify-content: space-between;
    padding: 0 52px 0 69px;
    font-family: "Cabin", sans-serif;
    font-weight: 500;
    font-size: 22px;
    letter-spacing: 1px;
    color: var(--ink);
  }
</style>
</head>
<body>
  <div class="card">
    <div class="camo-field" role="img" aria-label="Green camouflage background"></div>
    <div class="rider-photo" role="img" aria-label="Armored rider on a white horse holding a lance, with a green glow"></div>
    <div class="vision-panel"></div>
    <div class="vision-title">GREY FALCON UNIT VISION</div>
    <p class="vision-text">A superbly fit, trained, disiplined, ready,<br>and adaptableunit, exercising mission<br>command and teamwork to aggressively<br>execute any misson and win!</p>
    <div class="motto-band">
      <span class="motto-left">ALWAYS TOWARD THE ENEMY</span>
      <span class="motto-right">STRIKE FIRST</span>
    </div>
  </div>
</body>
</html>
```